Real estate investor business card to retire young ;)!

I need a logo design and a business card. I am based in Montreal, Canada. I buy multi-family properties and do lots development. The final design should communicate that I am a problem solver and reliable.

This card will be given to other investors, to potential sellers and industry experts.

Target Market(s)

Real estate community, multi-family owners

Industry/Entity Type

Real Estate Development

Contact Information for Business Card

My name: Lorna Vickery
email: immo.lorna.vickery@quellmail.example
cellphone: (555) 274-3916

Logo Text

Gestion immobilière

Font styles to use
Sans Serif

Colors
3176b5

Requirements
Must have
• Within 1-2 seconds the person who sees my card should know that I buy properties and lot. Areas to for Phone number and email adress. I do not have a business name. The card should simply state my name and what I do. The logo should be remembered by the person who reads my card
Should not have
• Colors too bright. Too much small details. I want something balanced, bold without being agressive.

```html
<!DOCTYPE html>
<html lang="fr">
<head>
<meta charset="utf-8">
<title>Lorna Vickery – Carte d'affaires</title>
<link href="https://fonts.googleapis.com/css2?family=Saira+Condensed:wght@500;600;700&family=Roboto:wght@700;900&display=swap" rel="stylesheet">
<style>
  :root{
    --stage:#1d1d1e;
    --ink:#1b1b1b;
    --paper:#f2f2f2;
    --sky:#14a8e4;
    --white:#ffffff;
    --ghost:#dcdcdc;
    --rule:#2a2a2a;
  }
  *{box-sizing:border-box;margin:0;padding:0}
  html,body{width:1200px;height:1200px;overflow:hidden;background:var(--stage)}
  .stage{position:relative;width:1200px;height:1200px}
  .card{position:absolute;left:150px;width:900px;height:510px;overflow:hidden;box-shadow:0 14px 30px rgba(0,0,0,.45)}
  .card--front{top:60px;background:var(--ink)}
  .card--back{top:630px;background:var(--paper)}

  .identity{position:absolute;display:flex;align-items:center;gap:26px}
  .identity__mark{width:86px;height:86px;background:var(--sky);flex:none}
  .identity__name{font-family:"Saira Condensed",sans-serif;font-weight:700;font-size:76px;line-height:.9;letter-spacing:1px;text-transform:uppercase}
  .identity__role{font-family:"Saira Condensed",sans-serif;font-weight:600;font-size:23px;color:var(--sky);text-transform:uppercase;letter-spacing:.3px;margin-top:6px}

  .card--front .identity{left:150px;top:140px}
  .card--front .identity__name{color:var(--white)}

  .slogan{position:absolute;left:0;right:0;text-align:center;font-family:"Roboto",sans-serif;text-transform:uppercase}
  .slogan__fr{font-weight:900;font-size:33px;letter-spacing:1px;color:var(--sky)}
  .slogan__en{font-weight:700;font-size:22px;letter-spacing:1px;margin-top:2px}
  .card--front .slogan{top:330px}
  .card--front .slogan__en{color:var(--white)}

  .card--back .identity{left:60px;top:70px}
  .card--back .identity__name{color:var(--ink)}

  .ghost-mark{position:absolute;right:-10px;top:120px;font-family:"Saira Condensed",sans-serif;font-weight:700;font-size:330px;line-height:1;color:var(--ghost)}

  .contact{position:absolute;font-family:"Saira Condensed",sans-serif;font-weight:600;color:var(--ink);display:flex;align-items:center;gap:12px}
  .contact--phone{left:60px;top:300px;font-size:34px;letter-spacing:1px}
  .contact--email{right:60px;top:352px;font-size:27px;letter-spacing:1.5px;text-transform:uppercase}
  .contact svg{flex:none}
  .rule{position:absolute;height:2px}
  .rule--phone{left:60px;top:286px;width:430px;background:var(--rule)}
  .rule--email{right:60px;top:340px;width:440px;background:var(--sky)}

  .band{position:absolute;left:0;right:0;bottom:0;height:118px;background:var(--sky)}
  .card--back .slogan{top:14px}
  .card--back .slogan__fr,.card--back .slogan__en{color:var(--white)}
</style>
</head>
<body>
<main class="stage">
  <section class="card card--front">
    <div class="identity">
      <span class="identity__mark"></span>
      <div>
        <div class="identity__name">Lorna Vickery</div>
        <div class="identity__role">Investisseur immobilier / Real estate investment</div>
      </div>
    </div>
    <div class="slogan">
      <div class="slogan__fr">J'achète des multi-logements et des maisons</div>
      <div class="slogan__en">I buy multi-family properties and houses</div>
    </div>
  </section>

  <section class="card card--back">
    <div class="ghost-mark" aria-hidden="true">LV</div>
    <div class="identity">
      <span class="identity__mark"></span>
      <div>
        <div class="identity__name">Lorna Vickery</div>
        <div class="identity__role">Investisseur immobilier / Real estate investment</div>
      </div>
    </div>

    <span class="rule rule--phone"></span>
    <div class="contact contact--phone">
      <svg width="28" height="24" viewBox="0 0 28 24" aria-hidden="true">
        <path d="M2 8c0-4 24-4 24 0v3h-6V8H8v3H2z" fill="var(--sky)"/>
        <rect x="5" y="12" width="18" height="10" rx="2" fill="var(--sky)"/>
      </svg>
      <span>555-274-3916</span>
    </div>

    <span class="rule rule--email"></span>
    <div class="contact contact--email">
      <span>immo.lorna.vickery@quellmail.example</span>
      <svg width="32" height="22" viewBox="0 0 32 22" aria-hidden="true">
        <rect x="1" y="1" width="30" height="20" rx="2" fill="none" stroke="var(--sky)" stroke-width="2.5"/>
        <path d="M2 2l14 11L30 2" fill="none" stroke="var(--sky)" stroke-width="2.5"/>
      </svg>
    </div>

    <div class="band">
      <div class="slogan">
        <div class="slogan__fr">J'achète des multi-logements et des maisons</div>
        <div class="slogan__en">I buy multi-family properties and houses</div>
      </div>
    </div>
  </section>
</main>
</body>
</html>
```